eBook Cover Design Project - Midwinter Promises

We need an ebook cover design for our new digital only title for Lantern Press.

Lantern Press is Romance. Lantern will own Romance in digital-first as Bellweather owns Romance in print and ebook.

We are looking for FUN, MODERN, PREMIUM designs. Please keep the look clean and edgy but have fun with it; be flirty - it's romance!!!

Target Market(s)

30-55 year old women.

Industry/Entity Type

Digital

Requirements
Must have
• Must work as a black and white image as well as a colour image.
- Must be easily viewed at thumbnail size.
- Title must always be larger than the author name. Both must appear on cover.
- Final file should be a JPEG supplied at 2240 pixels (H) X 1400 pixels (W).
- See attached document for story report.
- If using people on the cover refer to character traits in story report.
Should not have
• Offensive or pornographic content.
- Too many elements – keep it simple.

```html
<!DOCTYPE html>
<html lang="en">
<head>
<meta charset="utf-8">
<title>Midwinter Promises – Cover Options</title>
<link rel="stylesheet" href="https://fonts.googleapis.com/css2?family=Open+Sans:wght@700&family=Tinos&display=swap">
<style>
  :root {
    --stage: #e4e4e4;
    --cover-black: #050505;
    --author-white: #ffffff;
    --title-white: #ffffff;
    --title-shadow: #1a1a1a;
    --silver-light: #e2e2e2;
    --silver-dark: #6a6a6a;
    --ruby: #d0101a;
    --ruby-edge: #ffffff;
    --mono-skin: #c8c8c8;
    --mono-dress: #7a7a7a;
    --mono-suit: #2c2c2c;
    --mono-light: #bdbdbd;
    --mono-mid: #555555;
    --night-blue: #14244a;
    --glow-blue: #5a86e6;
    --skin-warm: #caa17e;
    --dress-bronze: #6e5640;
    --suit-navy: #16203c;
    --city-red: #b8242a;
    --city-amber: #e08a3c;
  }
  * { box-sizing: border-box; margin: 0; padding: 0; }
  html, body {
    width: 1200px;
    height: 900px;
    overflow: hidden;
    background: var(--stage);
  }
  .showcase {
    position: relative;
    width: 1200px;
    height: 900px;
  }
  .cover {
    position: absolute;
    top: 51px;
    width: 497px;
    height: 798px;
    background: var(--cover-black);
    overflow: hidden;
  }
  .cover--mono { left: 80px; }
  .cover--colour { left: 627px; }

  .cover__photo {
    position: absolute;
    left: 0;
    top: 0;
    width: 100%;
    height: 100%;
  }
  .cover--mono .cover__photo {
    background:
      radial-gradient(ellipse 13% 9% at 34% 36%, var(--mono-skin) 0%, transparent 75%),
      radial-gradient(ellipse 12% 9% at 58% 35%, var(--mono-light) 0%, transparent 75%),
      radial-gradient(ellipse 20% 30% at 32% 62%, var(--mono-dress) 0%, transparent 78%),
      radial-gradient(ellipse 26% 42% at 66% 64%, var(--mono-suit) 0%, transparent 80%),
      radial-gradient(ellipse 14% 9% at 6% 52%, var(--mono-light) 0%, transparent 85%),
      radial-gradient(ellipse 12% 8% at 98% 42%, #ffffff 0%, transparent 85%),
      radial-gradient(ellipse 12% 10% at 4% 70%, var(--mono-mid) 0%, transparent 85%),
      radial-gradient(ellipse 60% 40% at 50% 58%, #3a3a3a 0%, transparent 80%),
      linear-gradient(180deg, var(--cover-black) 0%, #101010 25%, #1c1c1c 55%, #0c0c0c 100%);
  }
  .cover--colour .cover__photo {
    background:
      radial-gradient(ellipse 13% 9% at 34% 36%, var(--skin-warm) 0%, transparent 75%),
      radial-gradient(ellipse 12% 9% at 58% 35%, #b08a6c 0%, transparent 75%),
      radial-gradient(ellipse 16% 22% at 24% 40%, var(--glow-blue) 0%, transparent 75%),
      radial-gradient(ellipse 20% 30% at 32% 62%, var(--dress-bronze) 0%, transparent 78%),
      radial-gradient(ellipse 26% 42% at 66% 64%, var(--suit-navy) 0%, transparent 80%),
      radial-gradient(ellipse 14% 9% at 6% 52%, var(--city-amber) 0%, transparent 85%),
      radial-gradient(ellipse 12% 10% at 8% 66%, var(--city-red) 0%, transparent 85%),
      radial-gradient(ellipse 12% 8% at 98% 42%, #f4e0c8 0%, transparent 85%),
      radial-gradient(ellipse 12% 12% at 94% 70%, var(--city-red) 0%, transparent 85%),
      radial-gradient(ellipse 60% 40% at 50% 58%, var(--night-blue) 0%, transparent 80%),
      linear-gradient(180deg, var(--cover-black) 0%, #07091a 25%, #0e1430 55%, #06080f 100%);
  }

  .cover__author {
    position: absolute;
    top: 29px;
    left: 0;
    width: 100%;
    text-align: center;
    font-family: "Open Sans", Arial, sans-serif;
    font-weight: 700;
    font-size: 24px;
    line-height: 32px;
    color: var(--author-white);
  }
  .cover__title {
    position: absolute;
    top: 72px;
    left: 0;
    width: 100%;
    text-align: center;
    font-family: "Tinos", "Times New Roman", serif;
    font-weight: 400;
  }
  .cover__title-lead {
    display: block;
    font-size: 84px;
    line-height: 86px;
    letter-spacing: -2px;
  }
  .cover--mono .cover__title-lead {
    color: var(--silver-light);
    background: linear-gradient(180deg, var(--silver-light) 0%, var(--silver-dark) 100%);
    -webkit-background-clip: text;
    background-clip: text;
    -webkit-text-fill-color: transparent;
    -webkit-text-stroke: 1px #f2f2f2;
  }
  .cover--colour .cover__title-lead {
    color: var(--ruby);
    -webkit-text-stroke: 1px var(--ruby-edge);
  }
  .cover__title-main {
    display: block;
    font-size: 78px;
    line-height: 80px;
    letter-spacing: -1px;
    color: var(--title-white);
    text-shadow: 3px 3px 2px var(--title-shadow);
  }
</style>
</head>
<body>
  <main class="showcase">
    <article class="cover cover--mono">
      <div class="cover__photo" role="img" aria-label="Black and white photograph of a smiling couple standing forehead to forehead, holding hands, against a night city with soft bokeh lights"></div>
      <p class="cover__author">Maren Castell</p>
      <h1 class="cover__title">
        <span class="cover__title-lead">Midwinter</span>
        <span class="cover__title-main">Promises</span>
      </h1>
    </article>

    <article class="cover cover--colour">
      <div class="cover__photo" role="img" aria-label="Colour photograph of a smiling couple standing forehead to forehead, holding hands, rim-lit in blue against warm red and amber city bokeh at night"></div>
      <p class="cover__author">Maren Castell</p>
      <h1 class="cover__title">
        <span class="cover__title-lead">Midwinter</span>
        <span class="cover__title-main">Promises</span>
      </h1>
    </article>
  </main>
</body>
</html>
```